Plumbing Company business card design

Create a business card for our plumbing company. Following info needs to be present

Website-prairiepipeworks.com
Email- contact@prairiepipeworks-mail.com
Phone-515-394-2068
Address-4817 NW Cobalt Blvd STE K
Ankeny, Iowa 50347

```html
<!DOCTYPE html>
<html lang="en">
<head>
<meta charset="utf-8">
<title>Prairie Pipeworks – Business Card</title>
<link href="https://fonts.googleapis.com/css2?family=Montserrat:wght@300;400;700&display=swap" rel="stylesheet">
<style>
  :root {
    --canvas-bg: #959595;
    --card-blue: #0a4f9c;
    --pattern-dark: #084785;
    --pattern-light: #1d63ab;
    --brand-red: #ee2424;
    --brand-blue: #0b4e99;
    --white: #ffffff;
    --ink: #333333;
    --muted: #7a7a7a;
    --rule: #d0d0d0;
  }
  * { box-sizing: border-box; margin: 0; padding: 0; }
  html, body { width: 1200px; height: 1000px; overflow: hidden; }
  body {
    background: var(--canvas-bg);
    font-family: "Montserrat", sans-serif;
    position: relative;
  }
  .card {
    position: absolute;
    left: 293px;
    width: 615px;
    height: 350px;
    border-radius: 26px;
    overflow: hidden;
  }
  .card--front { top: 100px; background: var(--card-blue); }
  .card--back { top: 511px; background: var(--white); }

  .monogram-pattern {
    position: absolute;
    inset: 0;
    background:
      radial-gradient(ellipse at 85% 30%, rgba(255,255,255,0.08) 0%, rgba(255,255,255,0) 60%),
      linear-gradient(90deg, var(--pattern-dark) 0%, var(--card-blue) 45%, var(--pattern-light) 100%);
  }
  .front-brand {
    position: absolute;
    left: 255px;
    top: 215px;
    height: 56px;
    display: flex;
    align-items: center;
    gap: 12px;
  }
  .front-brand__dot {
    width: 54px; height: 54px; border-radius: 50%;
    background: var(--white);
  }
  .front-brand__name {
    color: var(--white);
    font-weight: 700;
    font-size: 21px;
    letter-spacing: 1px;
    line-height: 1;
  }

  .back-brand {
    position: absolute;
    left: 44px;
    top: 118px;
    width: 222px;
    display: flex;
    flex-direction: column;
    align-items: center;
    gap: 12px;
  }
  .back-brand__dot {
    width: 70px; height: 70px; border-radius: 50%;
    background: var(--brand-red);
  }
  .back-brand__name {
    color: var(--brand-blue);
    font-weight: 700;
    font-size: 19px;
    letter-spacing: 0.5px;
    text-align: center;
    line-height: 1.15;
  }

  .person {
    position: absolute;
    left: 305px;
    top: 117px;
  }
  .person__name {
    font-weight: 700;
    font-size: 15px;
    letter-spacing: 3.6px;
    color: var(--ink);
  }
  .person__role {
    font-weight: 300;
    font-size: 15px;
    letter-spacing: 2px;
    color: var(--ink);
    margin-top: 1px;
  }
  .contacts {
    list-style: none;
    margin-top: 15px;
  }
  .contacts li {
    display: flex;
    align-items: center;
    gap: 9px;
    font-size: 14px;
    color: var(--muted);
    height: 23.5px;
    white-space: nowrap;
  }
  .contacts svg { width: 17px; height: 15px; flex: none; }

  .address-rule {
    position: absolute;
    left: 44px; right: 42px;
    top: 297px;
    border-top: 1px solid var(--rule);
  }
  .address {
    position: absolute;
    left: 0; right: 0;
    top: 313px;
    text-align: center;
    font-size: 15px;
    color: var(--muted);
  }
</style>
</head>
<body>

<section class="card card--front">
  <div class="monogram-pattern" role="img" aria-label="Faint embossed repeated monogram pattern across the blue card face"></div>
  <div class="front-brand">
    <span class="front-brand__dot"></span>
    <span class="front-brand__name">PRAIRIE PIPEWORKS</span>
  </div>
</section>

<section class="card card--back">
  <div class="back-brand">
    <span class="back-brand__dot"></span>
    <span class="back-brand__name">PRAIRIE PIPEWORKS</span>
  </div>

  <div class="person">
    <p class="person__name">NAME SURNAME</p>
    <p class="person__role">Position</p>
    <ul class="contacts">
      <li>
        <svg viewBox="0 0 17 15" aria-hidden="true"><rect x="5" y="0.5" width="7" height="13.5" rx="1.5" fill="none" stroke="var(--brand-red)" stroke-width="1.6"/><circle cx="8.5" cy="11.6" r="0.9" fill="var(--brand-red)"/></svg>
        515-394-2068
      </li>
      <li>
        <svg viewBox="0 0 17 15" aria-hidden="true"><rect x="1.5" y="3" width="14" height="10" fill="var(--brand-red)"/><path d="M1.5 3 L8.5 9 L15.5 3" fill="none" stroke="var(--white)" stroke-width="1.2"/></svg>
        contact@prairiepipeworks-mail.com
      </li>
      <li>
        <svg viewBox="0 0 17 15" aria-hidden="true"><circle cx="8.5" cy="7.5" r="6" fill="var(--brand-red)"/><g fill="none" stroke="var(--white)" stroke-width="0.9"><ellipse cx="8.5" cy="7.5" rx="2.6" ry="6"/><line x1="2.5" y1="7.5" x2="14.5" y2="7.5"/><line x1="3.4" y1="4.6" x2="13.6" y2="4.6"/><line x1="3.4" y1="10.4" x2="13.6" y2="10.4"/></g></svg>
        prairiepipeworks.com
      </li>
    </ul>
  </div>

  <div class="address-rule"></div>
  <p class="address">4817 NW Cobalt Blvd , STE K Ankeny, Iowa 50347</p>
</section>

</body>
</html>
```